Flyer für unser Jubiläumscamp "herbstcamp"

Am 10. - 14.10.2022 und 17. - 21. 10.2022 organisieren wir je eine Woche ein Fussballcamp für Kinder ab 5 Jahren bis 12 Jahren. Ebenfalls feiern wir unser 5 jähriges Jubiläum und bieten deshalb das Camp für 300 statt 350 CHF an.
Für dieses Camp (mit dieses 2 Angeboten) möchten wir einen speziellen Flyer haben. Der Flyedr sollte Kinder freundlich aber auch modern sein. Wir bieten auch ein Leistungs, Girls Only sowie ein Goalicamp. (eventuell ist dies aber zu überlastet dan)
Infos zu unseren Camps: https://balltaler.ch/events/2022-sommercamps-juli/

Kinder, 5-12 Jahre

• Logo, Fun Kidscamp
• Gleiches wie der Flyer angehängt.

```html
<!DOCTYPE html>
<html lang="de">
<head>
<meta charset="utf-8">
<title>Balltaler Jubiläumscamp 2022</title>
<link rel="stylesheet" href="https://fonts.googleapis.com/css2?family=Alfa+Slab+One&family=Kaushan+Script&family=Roboto+Condensed:wght@500;700&family=Roboto:wght@400;500&display=swap">
<style>
  :root {
    --blue: #1b3f9a;
    --orange: #f39419;
    --yellow: #f8b21c;
    --white: #ffffff;
    --paper: #fbfbfb;
    --stage: #e6e6e6;
    --rule: #9aa3b5;
  }
  * { box-sizing: border-box; margin: 0; padding: 0; }
  html, body { width: 1200px; height: 800px; overflow: hidden; }
  body { background: var(--stage); position: relative; font-family: "Roboto", sans-serif; }

  .flyer {
    position: absolute; left: 331px; top: 20px;
    width: 538px; height: 760px;
    background: var(--paper); overflow: hidden;
  }
  .flyer-shapes { position: absolute; inset: 0; width: 538px; height: 760px; }

  .brand {
    position: absolute; left: 0; top: 56px; width: 116px;
    text-align: center; color: var(--white);
    font-family: "Alfa Slab One", serif; font-size: 17px;
  }

  .mascot {
    position: absolute; left: 10px; top: 148px; width: 218px; height: 370px;
    border-radius: 110px 110px 30px 30px;
    background: linear-gradient(180deg, #f7a43a 0%, #f6c23a 40%, #2e4fb0 62%, #f08a2a 82%, #f6c23a 100%);
    opacity: .9;
  }

  .anniversary-number {
    position: absolute; left: 158px; top: 96px;
    font-family: "Alfa Slab One", serif; font-size: 160px; line-height: 1;
    color: var(--blue);
  }
  .headline {
    position: absolute; left: 252px; top: 118px;
    transform: rotate(-16deg); transform-origin: left top;
    font-family: "Alfa Slab One", serif; line-height: 1; white-space: nowrap;
  }
  .headline .line-1 { font-size: 34px; color: var(--orange); }
  .headline .line-2 { font-size: 38px; color: var(--yellow); margin-top: 2px; margin-left: 10px; }
  .offer {
    position: absolute; left: 330px; top: 208px;
    transform: rotate(-16deg); transform-origin: left top;
    border-top: 1.5px solid var(--rule); padding-top: 5px; width: 172px;
    font-family: "Roboto Condensed", sans-serif; font-weight: 700;
    font-size: 15px; line-height: 1.05; color: var(--blue); white-space: nowrap;
  }
  .offer-script {
    position: absolute; left: 240px; top: 222px; width: 90px; height: 46px;
    text-align: center; transform: rotate(-62deg); transform-origin: center;
    font-family: "Kaushan Script", cursive; font-size: 36px; line-height: 46px; color: var(--yellow);
  }

  .camp-badge {
    position: absolute; left: 282px; top: 298px; width: 236px;
    text-align: center; font-family: "Alfa Slab One", serif; line-height: 1;
  }
  .camp-badge .kicker { font-size: 19px; color: var(--yellow); }
  .camp-badge .title { font-size: 21px; color: var(--white); margin-top: 2px; padding-bottom: 9px; border-bottom: 1.5px solid var(--white); }
  .camp-badge .year { font-size: 80px; color: var(--yellow); padding: 6px 0 4px; border-bottom: 1.5px solid var(--white); letter-spacing: 2px; }
  .camp-badge .dates { font-size: 17px; color: var(--white); margin-top: 8px; white-space: nowrap; }

  .camp-table {
    position: absolute; left: 19px; top: 530px; width: 503px;
    border-collapse: collapse; background: var(--white);
    font-family: "Roboto Condensed", sans-serif; font-weight: 500; font-size: 8.6px;
  }
  .camp-table th {
    background: var(--blue); color: var(--white); text-align: left;
    font-family: "Alfa Slab One", serif; font-weight: 400; font-size: 15px;
    height: 33px; padding: 0 12px;
  }
  .camp-table td { height: 27px; padding: 0 9px; border: 1.2px solid var(--blue); }
  .camp-table .col-details { width: 257px; }
  .camp-table .col-price { width: 122px; }
  .row-accent td { color: var(--orange); }
  .row-plain td { color: var(--blue); }

  .contact {
    position: absolute; left: 0; right: 0; top: 704px;
    display: flex; justify-content: center; gap: 22px;
    font-size: 15px; color: var(--blue);
  }
  .contact-item { display: flex; align-items: center; gap: 7px; }
  .contact-item svg { width: 20px; height: 20px; }
</style>
</head>
<body>
  <main class="flyer">
    <svg class="flyer-shapes" viewBox="0 0 538 760" aria-hidden="true">
      <polygon points="110,0 538,0 538,8 122,82" fill="var(--yellow)"/>
      <polygon points="119,86 538,4 538,14 121,96" fill="var(--blue)"/>
      <circle cx="56" cy="66" r="70" fill="var(--yellow)"/>
      <circle cx="54" cy="62" r="66" fill="var(--blue)"/>
      <circle cx="420" cy="456" r="197" fill="var(--yellow)"/>
      <circle cx="424" cy="456" r="190" fill="var(--blue)"/>
      <polygon points="0,514 538,504 538,760 0,760" fill="var(--yellow)"/>
      <rect x="0" y="746" width="538" height="14" fill="var(--blue)"/>
    </svg>

    <div class="brand">Balltaler</div>

    <div class="mascot" role="img" aria-label="Illustration: Löwen-Maskottchen im blauen Trikot mit Fussball, Daumen hoch"></div>

    <div class="anniversary-number">5</div>
    <div class="headline">
      <div class="line-1">GEBURTSTAG</div>
      <div class="line-2">BALLTALER</div>
    </div>
    <div class="offer-script">Biete</div>
    <div class="offer">DAS CAMP FÜR 300<br>STATT 350 CHF AN.</div>

    <section class="camp-badge">
      <div class="kicker">HERBSTCAMP &amp;</div>
      <div class="title">LEISTUNGSCAMP</div>
      <div class="year">2022</div>
      <div class="dates">10.–14. &amp; 17.–21. OKTOBER</div>
    </section>

    <table class="camp-table">
      <thead>
        <tr><th class="col-details">DETAILS</th><th class="col-price">PREIS</th><th>ANZAHL</th></tr>
      </thead>
      <tbody>
        <tr class="row-accent"><td>GIRLS-ONLY (5-12 JAHRE) (OERLIKON-ZH)</td><td>CHF 350</td><td>AUSVERKAUFT</td></tr>
        <tr class="row-plain"><td>HERBSTCAMP I (5-12 JAHRE) (OERLIKON-ZH)</td><td>CHF 350</td><td>AUSVERKAUFT</td></tr>
        <tr class="row-accent"><td>TORWARTCAMP (7-12 JAHRE) (OERLIKON-ZH)</td><td>CHF 350</td><td>AUSVERKAUFT</td></tr>
        <tr class="row-plain"><td>LEISTUNGS-CAMP (STUFE E+D JUNIOREN) (OERLIKON-ZH)</td><td>CHF 450</td><td>ABGELAUFEN</td></tr>
        <tr class="row-accent"><td>LEISTUNGS-TORWARTCAMP (11-14 JAHRE) (OERLIKON-ZH)</td><td>CHF 450</td><td>AUSVERKAUFT</td></tr>
      </tbody>
    </table>

    <footer class="contact">
      <span class="contact-item">
        <svg viewBox="0 0 20 20" aria-hidden="true"><circle cx="10" cy="10" r="10" fill="var(--blue)"/><rect x="5" y="6.5" width="10" height="7" rx="1" fill="none" stroke="#fff" stroke-width="1.3"/><polyline points="5.5,7 10,10.8 14.5,7" fill="none" stroke="#fff" stroke-width="1.3"/></svg>
        info@balltaler.ch
      </span>
      <span class="contact-item">
        <svg viewBox="0 0 20 20" aria-hidden="true"><circle cx="10" cy="10" r="10" fill="var(--blue)"/><circle cx="10" cy="10" r="5.5" fill="none" stroke="#fff" stroke-width="1.2"/><ellipse cx="10" cy="10" rx="2.4" ry="5.5" fill="none" stroke="#fff" stroke-width="1.2"/><line x1="4.5" y1="10" x2="15.5" y2="10" stroke="#fff" stroke-width="1.2"/></svg>
        www.balltaler.ch
      </span>
    </footer>
  </main>
</body>
</html>
```